Business Card Design Project

We need a business card for our IT services provider business. We provide services to small and medium business, and would like something that reflects the color scheme / branding on our recently updated website - www.tallobrix.com.au

The card type we have chosen is a matte laminated double sided configuration at 86mm x 54mm on 350 GSM cardboard.
Updates

Target Market(s)

Small and Medium Business owners

Industry/Entity Type

Business

Requirements
Must have
• *Details on all cards*

Company Name: Tallobrix Pty Ltd
ABN: 52 683 914 207
Address: 47-49 Pembury Street, Ashcombe Vale, Victoria 3172
Phone: 1300 GRAB UP
Fax: 03 9417 6258
Website: www.tallobrix.com.au
Logo/Handprint Icon

*Person Specific*

```html
<!DOCTYPE html>
<html lang="en">
<head>
<meta charset="utf-8">
<title>Tallobrix Business Card</title>
<link rel="stylesheet" href="https://fonts.googleapis.com/css2?family=Arimo:wght@400;700&display=swap">
<style>
  :root {
    --brand-blue: #1a5b9c;
    --brand-blue-deep: #124a84;
    --brand-blue-soft: #2d6fb0;
    --paper: #f3f3f3;
    --paper-shade: #dcdcdc;
    --ink: #1f1f1f;
    --white: #ffffff;
    --backdrop: #e9ebee;
  }
  * { box-sizing: border-box; margin: 0; padding: 0; }
  html, body {
    width: 1200px; height: 984px; overflow: hidden;
    background: var(--backdrop);
    font-family: "Arimo", Arial, sans-serif;
  }
  .stage { position: relative; width: 1200px; height: 984px; }
  .card {
    position: absolute; left: 250px; width: 700px; height: 440px;
    overflow: hidden; box-shadow: 0 6px 18px rgba(0,0,0,0.18);
  }
  .card--back { top: 32px; background: linear-gradient(160deg, var(--brand-blue-soft), var(--brand-blue-deep)); }
  .card--front { top: 512px; background: linear-gradient(180deg, var(--white), var(--paper) 55%, var(--paper-shade)); }

  /* Back */
  .back-mark {
    position: absolute; left: 40px; top: 70px; width: 230px; height: 230px;
    border-radius: 50%; background: rgba(255,255,255,0.08);
  }
  .back-logo {
    position: absolute; left: 0; right: 0; top: 160px; text-align: center;
    font-weight: 700; font-size: 78px; letter-spacing: 4px; color: var(--paper);
  }
  .back-rule {
    position: absolute; left: 200px; right: 200px; top: 272px; height: 2px;
    background: linear-gradient(90deg, transparent, rgba(255,255,255,0.8), transparent);
  }
  .back-web {
    position: absolute; left: 0; right: 0; top: 288px; text-align: center;
    font-size: 20px; color: var(--paper); letter-spacing: 1px;
  }

  /* Front */
  .front-logo {
    position: absolute; left: 48px; top: 36px;
    font-weight: 700; font-size: 44px; letter-spacing: 2px; color: var(--ink);
  }
  .front-mark {
    position: absolute; left: -40px; top: 110px; width: 200px; height: 200px;
    border-radius: 50%; background: var(--brand-blue); z-index: 2;
    box-shadow: 0 0 0 6px var(--white);
  }
  .person {
    position: absolute; right: 36px; top: 136px; text-align: right;
  }
  .person__name { font-weight: 700; font-size: 34px; color: var(--brand-blue); margin-bottom: 6px; }
  .person__line {
    display: flex; justify-content: flex-end; align-items: center; gap: 10px;
    font-size: 21px; color: var(--ink); line-height: 1.4;
  }
  .person__line svg { width: 18px; height: 18px; }
  .band {
    position: absolute; left: 0; right: 0; top: 272px; bottom: 0;
    background: var(--brand-blue); color: var(--white);
    padding: 16px 36px 0 180px; font-size: 18px; line-height: 1.5;
    white-space: nowrap;
  }
  .band__row { display: flex; justify-content: space-between; }
  .band__company { font-weight: 700; }
  .band__rule { border-top: 2px dashed rgba(255,255,255,0.6); margin: 4px 0 6px; }
  .band b { font-weight: 700; }
</style>
</head>
<body>
<main class="stage">
  <section class="card card--back" aria-label="Card back">
    <div class="back-mark"></div>
    <div class="back-logo">Tallobrix</div>
    <div class="back-rule"></div>
    <div class="back-web">www.tallobrix.com.au</div>
  </section>

  <section class="card card--front" aria-label="Card front">
    <div class="front-logo">Tallobrix</div>
    <div class="front-mark"></div>
    <div class="person">
      <div class="person__name">Marcus HALE</div>
      <div class="person__line">1300 482 915
        <svg viewBox="0 0 18 18" aria-hidden="true"><rect x="5" y="1" width="8" height="16" rx="1.5" fill="none" stroke="var(--brand-blue)" stroke-width="1.6"/><line x1="7.5" y1="14" x2="10.5" y2="14" stroke="var(--brand-blue)" stroke-width="1.6"/></svg>
      </div>
      <div class="person__line">marcus@tallobrix.com.au
        <svg viewBox="0 0 18 18" aria-hidden="true"><rect x="1" y="4" width="16" height="11" fill="none" stroke="var(--brand-blue)" stroke-width="1.6"/><polyline points="1,4 9,11 17,4" fill="none" stroke="var(--brand-blue)" stroke-width="1.6"/></svg>
      </div>
    </div>
    <div class="band">
      <div class="band__row"><span class="band__company">TALLOBRIX PTY LTD</span><span>| ABN: 52 683 914 207</span></div>
      <div class="band__rule"></div>
      <div>47-49 Pembury Street, Ashcombe Vale, Victoria 3172</div>
      <div class="band__row"><span><b>Phone:</b> 1300 GRAB UP</span><span>| <b>Fax:</b> 03 9417 6258</span></div>
    </div>
  </section>
</main>
</body>
</html>
```